Looking for a cool & simple business-card-design for digital agency

Hi!

We are a web agency that offers Reputation Management, Vextra & Seo Services and software development. We like cool things, we like innovative styles.

We have uploaded our logo.

Project Deadline Extended Reason: Client does not want any designs with the colorful logo. Please send us submissions ONLY with the blac and white logo. What the client would like to see:1) Back of the card: is a silver logo on a black background2) front of the card with all the data, please use white background and black logo thank you Added Friday, May 8, 2015

```html
<!DOCTYPE html>
<html lang="en">
<head>
<meta charset="utf-8">
<title>Nordwerk AG – Stationery</title>
<link rel="stylesheet" href="https://fonts.googleapis.com/css2?family=Open+Sans:wght@400;700&display=swap">
<style>
  :root {
    --backdrop: #e8e8e9;
    --paper: #fbfbfb;
    --paper-shade: #f1f1f1;
    --ink: #1a1a1a;
    --band: #0c0c0c;
    --silver: #c9c9c9;
    --faint: #e7e7e7;
    --muted: #555555;
  }
  * { margin: 0; padding: 0; box-sizing: border-box; }
  html, body { width: 1200px; height: 800px; overflow: hidden; }
  body {
    position: relative;
    background: var(--backdrop);
    font-family: "Open Sans", Arial, sans-serif;
    color: var(--ink);
  }
  .piece { position: absolute; background: var(--paper); overflow: hidden; }

  /* brand name block */
  .brand { position: absolute; display: flex; align-items: center; gap: 6px; }
  .brand-mark { width: 14px; height: 14px; background: var(--ink); flex: none; }
  .brand-text { display: flex; flex-direction: column; line-height: 1; }
  .brand-name { font-weight: 700; font-size: 15px; letter-spacing: 0.3px; }
  .brand-tagline { font-weight: 400; font-size: 7.5px; letter-spacing: 2.2px; margin-top: 3px; }

  .faint-square { position: absolute; background: var(--faint); }

  /* folder */
  .folder { left: 262px; top: 95px; width: 270px; height: 432px; }
  .folder-flap { position: absolute; left: 246px; top: 0; width: 24px; height: 100%; background: var(--paper-shade); border-left: 1px solid #dcdcdc; }
  .folder .brand { left: 66px; top: 52px; }
  .folder .faint-square { left: 14px; top: 240px; width: 190px; height: 190px; }

  /* letterhead */
  .letterhead { left: 627px; top: 97px; width: 290px; height: 410px; }
  .letterhead .brand { left: 28px; top: 22px; }
  .letterhead .brand-name { font-size: 13px; }
  .letterhead .brand-tagline { font-size: 6.5px; letter-spacing: 1.9px; }
  .letter-body { position: absolute; left: 25px; top: 102px; width: 243px; font-size: 5.6px; line-height: 7.9px; text-align: justify; }
  .letter-body p { margin-bottom: 7.9px; }
  .letter-greeting { margin-bottom: 10px !important; }
  .signature { position: absolute; left: 28px; top: 306px; width: 88px; height: 18px; background: linear-gradient(90deg, #d6d6d6, #ececec); }
  .signer-role { position: absolute; left: 28px; top: 334px; font-size: 6px; }
  .letterhead .faint-square { left: 196px; top: 302px; width: 86px; height: 86px; }
  .contact-row { position: absolute; left: 28px; top: 374px; display: flex; gap: 18px; font-size: 5px; line-height: 7px; color: var(--muted); }
  .address-band { position: absolute; left: 0; bottom: 0; width: 100%; height: 18px; background: var(--band); color: #fff; font-size: 5px; padding: 6px 0 0 28px; }

  /* compliment slip */
  .slip { left: 223px; top: 562px; width: 304px; height: 153px; }
  .slip .brand { left: 12px; top: 16px; }
  .slip .brand-name { font-size: 12px; }
  .slip .brand-tagline { font-size: 6px; letter-spacing: 1.8px; }
  .slip .faint-square { left: 232px; top: 58px; width: 66px; height: 76px; }
  .slip .address-band { height: 17px; padding-left: 14px; }

  /* envelope */
  .envelope { left: 575px; top: 561px; width: 303px; height: 154px; background: var(--paper-shade); }
  .envelope-flap { position: absolute; left: 0; top: 0; }
  .envelope-mark { position: absolute; left: 145px; top: 18px; width: 13px; height: 13px; background: #fff; }

  /* business cards */
  .card-back { left: 914px; top: 560px; width: 101px; height: 67px; background: var(--band); }
  .card-back .brand { left: 14px; top: 25px; gap: 4px; }
  .card-back .brand-mark { width: 8px; height: 8px; background: var(--silver); }
  .card-back .brand-name { font-size: 8px; color: var(--silver); }
  .card-back .brand-tagline { font-size: 3.6px; letter-spacing: 1px; color: var(--silver); margin-top: 2px; }

  .card-front { left: 914px; top: 655px; width: 101px; height: 72px; }
  .card-front .faint-square { left: 28px; top: 10px; width: 48px; height: 52px; }
  .card-front-rotated { position: absolute; left: 0; top: 72px; width: 72px; height: 101px; transform: rotate(-90deg); transform-origin: 0 0; }
  .card-front .brand { left: 6px; top: 6px; gap: 3px; }
  .card-front .brand-mark { width: 6px; height: 6px; }
  .card-front .brand-name { font-size: 6px; }
  .card-front .brand-tagline { font-size: 2.8px; letter-spacing: 0.6px; margin-top: 1px; }
  .employee { position: absolute; left: 6px; top: 24px; font-size: 3.4px; line-height: 4.4px; }
  .card-contact { position: absolute; left: 6px; bottom: 6px; font-size: 3px; line-height: 4px; color: var(--muted); }
</style>
</head>
<body>

  <section class="piece folder" aria-label="Presentation folder">
    <div class="faint-square"></div>
    <div class="folder-flap"></div>
    <div class="brand">
      <span class="brand-mark"></span>
      <span class="brand-text">
        <span class="brand-name">Nordwerk AG</span>
        <span class="brand-tagline">DIGITALE STRATEGIEN</span>
      </span>
    </div>
  </section>

  <section class="piece letterhead" aria-label="Letterhead">
    <div class="brand">
      <span class="brand-mark"></span>
      <span class="brand-text">
        <span class="brand-name">Nordwerk AG</span>
        <span class="brand-tagline">DIGITALE STRATEGIEN</span>
      </span>
    </div>
    <div class="faint-square"></div>
    <div class="letter-body">
      <p class="letter-greeting">Dear Client</p>
      <p>We are pleased to share our proposal for the coming season. Our team has reviewed your goals and prepared a clear plan for search, reputation and software work. Each stage is listed with its timing, its cost and the people who will lead it. We will keep you informed with short weekly reports and open calls whenever you need them. Please read the details below.</p>
      <p>Our first step is a full audit of your current website and online presence. We check speed, structure, content and the way your brand appears in search results. From there we build a plan that fits your budget and your market. Every change is tested before launch, and every result is measured so that you can see what works and why it matters.</p>
      <p>Thank you for the trust you have placed in our agency. We look forward to working with you and your team over the months ahead. If you have any questions about this proposal, please contact us at any time by phone or email. We will be glad to arrange a meeting at your office or ours.</p>
    </div>
    <div class="signature" role="img" aria-label="Handwritten signature of the managing director"></div>
    <p class="signer-role">Managing Director</p>
    <div class="contact-row">
      <span>T: 123 555 0142<br>F: 123 555 0143</span>
      <span>E: info@nordwerk.com<br>www.nordwerk.com</span>
    </div>
    <div class="address-band">42 Harbor Lane Suite 210, Portland USA 97201</div>
  </section>

  <section class="piece slip" aria-label="Compliment slip">
    <div class="brand">
      <span class="brand-mark"></span>
      <span class="brand-text">
        <span class="brand-name">Nordwerk AG</span>
        <span class="brand-tagline">DIGITALE STRATEGIEN</span>
      </span>
    </div>
    <div class="faint-square"></div>
    <div class="address-band">42 Harbor Lane Suite 210, Portland USA 97201</div>
  </section>

  <section class="piece envelope" aria-label="Envelope">
    <svg class="envelope-flap" width="303" height="52" viewBox="0 0 303 52">
      <path d="M0 0 H303 V22 Q303 26 297 28 L160 50 Q151 52 143 50 L6 28 Q0 26 0 22 Z" fill="#0c0c0c"/>
    </svg>
    <span class="envelope-mark"></span>
  </section>

  <section class="piece card-back" aria-label="Business card back">
    <div class="brand">
      <span class="brand-mark"></span>
      <span class="brand-text">
        <span class="brand-name">Nordwerk AG</span>
        <span class="brand-tagline">DIGITALE STRATEGIEN</span>
      </span>
    </div>
  </section>

  <section class="piece card-front" aria-label="Business card front">
    <div class="faint-square"></div>
    <div class="card-front-rotated">
      <div class="brand">
        <span class="brand-mark"></span>
        <span class="brand-text">
          <span class="brand-name">Nordwerk AG</span>
          <span class="brand-tagline">DIGITALE STRATEGIEN</span>
        </span>
      </div>
      <p class="employee">Employee Name<br>Title<br>M: 123 555 0142</p>
      <p class="card-contact">T: 123 555 0142<br>E: info@nordwerk.com<br>42 Harbor Lane Suite 210<br>Portland USA 97201</p>
    </div>
  </section>

</body>
</html>
```